Landing page for a cyber security service provider called 'Lumen Grove'

The client is a new cyber security company in need of a website landing page at lumengrove.example.

Their visual identity is modern, playful, clean and uncluttered and represents innovation, connectivity and approachability.

The company logo is provided in black (attached) but the client is open to changing the colour to align with the new website design.

The landing page needs to contain:
- A call to action with a 'Get Started' button
-Links to blank 'How it works', 'Products', 'Pricing', 'About Us' and 'Contact Us' pages (that we'll fill out later)

Target Market(s)

Medium to large businesses who probably don't understand cyber / cyber security but need their business to be protected.

Industry/Entity Type

Cyber Security

Coding

Coded - Design and coding required

Number of Pages Required

1 page

Font styles to use
Sans Serif
Other font styles liked:
• Helvetica

Requirements
Nice to have
• Hero banner at the top of the landing page.
Should not have
• Should not look like a traditional cyber / cyber security design (eg no dark blue/ black, red/black colour combinations). Please no military styles (eg no shields, cannons, swords, guns)

```html
<!DOCTYPE html>
<html lang="en">
<head>
<meta charset="utf-8">
<title>Lumen Grove — Cyber Security</title>
<link href="https://fonts.googleapis.com/css2?family=Montserrat:wght@400;500;600;700&display=swap" rel="stylesheet">
<style>
:root{
  --green:#7cb83a;
  --green-dark:#5f9a22;
  --hero-a:#2f4f40;
  --hero-b:#55826a;
  --hero-c:#3e6652;
  --hero-d:#263d32;
  --ink:#111111;
  --text:#333333;
  --muted:#666666;
  --line:#e3e3e3;
  --white:#ffffff;
  --black:#000000;
}
*{box-sizing:border-box;margin:0;padding:0}
html,body{width:1200px;height:5038px;overflow:hidden}
body{font-family:"Montserrat",Helvetica,Arial,sans-serif;color:var(--text);background:var(--white);position:relative}
.abs{position:absolute}
a{color:inherit;text-decoration:none}
.btn{position:absolute;display:flex;align-items:center;justify-content:center;gap:14px;border-radius:40px;background:var(--green);color:var(--white);font-weight:600;text-transform:uppercase;white-space:nowrap}
.btn .arrow{width:28px;height:28px;border-radius:50%;background:var(--white);display:flex;align-items:center;justify-content:center}
.btn .arrow svg{width:14px;height:14px}

/* header */
.site-header{position:absolute;left:0;top:0;width:1200px;height:100px;background:var(--white);z-index:2}
.brand-badge{position:absolute;left:70px;top:-85px;width:250px;height:270px;border-radius:50%;background:var(--white);z-index:3;display:flex;align-items:flex-end;justify-content:center;padding-bottom:62px}
.brand-name{font-weight:700;font-size:24px;color:var(--ink);display:flex;align-items:center;gap:8px;white-space:nowrap}
.brand-name .dot{width:12px;height:12px;border-radius:50%;background:var(--green)}
.main-nav{position:absolute;top:38px;left:560px;display:flex;gap:30px;font-size:11px;font-weight:500;color:var(--text);text-transform:uppercase;white-space:nowrap}
.main-nav a.active{color:var(--green);border-bottom:2px solid var(--green);padding-bottom:10px}
.nav-cta{left:1003px;top:29px;width:130px;height:40px;font-size:11px;font-weight:500}

/* hero */
.hero{position:absolute;left:0;top:100px;width:1200px;height:677px;background:linear-gradient(135deg,var(--hero-a) 0%,var(--hero-b) 42%,var(--hero-c) 68%,var(--hero-d) 100%)}
.hero h1{position:absolute;top:200px;width:100%;text-align:center;font-size:62px;font-weight:600;color:var(--white);white-space:nowrap}
.hero p{position:absolute;top:296px;left:300px;width:600px;text-align:center;font-size:16px;line-height:35px;color:var(--white)}
.hero .btn{left:481px;top:404px;width:237px;height:70px;font-size:18px}
.dots{position:absolute;top:582px;left:572px;display:flex;gap:4px}
.dots span{width:10px;height:10px;border-radius:50%;background:#a9b8ae}
.dots span:first-child{background:var(--white)}

/* section heads */
.kicker{position:absolute;width:100%;text-align:center;color:var(--green);font-size:24px;font-weight:600;display:flex;justify-content:center;align-items:center;gap:14px}
.kicker::before,.kicker::after{content:"";width:110px;height:2px;background:var(--green)}
.sec-title{position:absolute;width:100%;text-align:center;font-size:40px;font-weight:600;color:var(--ink)}
.sec-lead{position:absolute;left:160px;width:880px;text-align:center;font-size:13.5px;line-height:26px;color:var(--text)}

/* products */
.product-card{position:absolute;width:521px;height:453px;background:var(--white);box-shadow:0 2px 10px rgba(0,0,0,.13)}
.product-card .media{height:226px}
.product-card h3{margin-top:26px;text-align:center;font-size:23px;font-weight:500;color:var(--green)}
.product-card h4{margin-top:6px;text-align:center;font-size:17px;font-weight:600;color:var(--ink)}
.product-card p{margin:14px auto 0;width:460px;text-align:center;font-size:11px;line-height:21px;color:var(--muted)}
.product-card .btn{position:relative;margin:16px auto 0;width:128px;height:34px;font-size:10px;gap:8px}
.product-card .btn .arrow{width:16px;height:16px}
.product-card .btn .arrow svg{width:9px;height:9px}
.view-more{left:490px;top:2069px;width:219px;height:69px;background:var(--black);font-size:18px}

/* steps */
.step{position:absolute;width:240px;text-align:center}
.step .ring{margin:0 auto;width:116px;height:116px;border-radius:50%;border:3px solid var(--green);display:flex;align-items:center;justify-content:center}
.step .ring span{width:100px;height:100px;border-radius:50%;background:var(--green);color:var(--white);font-size:56px;font-weight:700;display:flex;align-items:center;justify-content:center}
.step h5{margin-top:26px;font-size:20px;font-weight:600;color:var(--ink);line-height:25px}
.step-arrow{position:absolute;top:2478px;width:150px;height:40px}

/* about */
.about-kicker{position:absolute;left:168px;top:2773px;font-size:20px;font-weight:600;color:var(--green);display:flex;align-items:center;gap:14px}
.about-kicker::after{content:"";width:56px;height:2px;background:var(--green)}
.about-title{position:absolute;left:168px;top:2803px;font-size:38px;font-weight:600;color:var(--ink);white-space:nowrap}
.about-text{position:absolute;left:168px;top:2880px;width:438px;font-size:13px;line-height:26.5px;color:var(--text);text-align:justify}
.about-btn{left:168px;top:3070px;width:150px;height:45px;font-size:12px;gap:10px}
.about-btn .arrow{width:20px;height:20px}
.about-visual{position:absolute;left:700px;top:2790px;width:320px;height:320px;border-radius:50%;background:radial-gradient(circle,#e8e8e8 0%,#b7a897 55%,#f4f4f4 100%);opacity:.8}

/* pricing */
.plan{position:absolute;top:3398px;width:299px;height:417px;background:var(--white);box-shadow:0 2px 10px rgba(0,0,0,.12)}
.plan .head{height:122px;background:var(--green);color:var(--white);text-align:center;padding-top:30px}
.plan .price{font-size:34px;font-weight:600}
.plan .per{font-size:18px}
.plan ul{list-style:none;margin:26px 0 0 50px}
.plan li{display:flex;align-items:center;gap:12px;font-size:13px;height:40px;color:var(--ink)}
.plan li i{width:28px;height:28px;border-radius:50%;border:1.5px solid var(--green);display:flex;align-items:center;justify-content:center}
.plan .btn{position:relative;margin:22px auto 0;width:200px;height:46px;font-size:15px}
.plan.featured{background:var(--black);box-shadow:none}
.plan.featured .head{background:var(--black)}
.plan.featured li{color:var(--white)}
.plan.featured li i{border-color:var(--white)}

/* contact */
.contact-band{position:absolute;left:0;top:3922px;width:250px;height:641px;background:var(--green)}
.contact-visual{position:absolute;left:58px;top:4090px;width:344px;height:344px;border-radius:50%;border:2px solid var(--green);padding:6px;background:var(--white)}
.contact-visual div{width:100%;height:100%;border-radius:50%;background:linear-gradient(135deg,#a9c4bb,#4f7566 50%,#2f4a40)}
.field{position:absolute;height:53px;background:var(--white);box-shadow:0 1px 6px rgba(0,0,0,.14);font-size:13px;color:#999;padding:18px 22px}
.submit{left:480px;top:4430px;width:207px;height:60px;font-size:16px}

/* footer */
.site-footer{position:absolute;left:0;top:4563px;width:1200px;height:475px;background:var(--black);color:var(--white)}
.foot-line{position:absolute;height:1px;background:#555}
.foot-nav{position:absolute;top:170px;display:flex;align-items:center;gap:32px;font-size:12px;font-weight:500;text-transform:uppercase;white-space:nowrap}
.foot-nav i{width:9px;height:9px;border-radius:50%;background:var(--green)}
.foot-brand{position:absolute;left:480px;top:158px;width:240px;font-size:28px;font-weight:700;display:flex;justify-content:center;align-items:center;gap:10px;white-space:nowrap}
.foot-brand .dot{width:12px;height:12px;border-radius:50%;background:var(--green)}
.contact-item{position:absolute;top:290px;display:flex;align-items:center;gap:14px;white-space:nowrap}
.contact-item .ic{width:66px;height:66px;border-radius:50%;background:var(--white);display:flex;align-items:center;justify-content:center}
.contact-item .ic svg{width:30px;height:30px}
.contact-item b{display:block;color:var(--green);font-size:17px;font-weight:500}
.contact-item small{font-size:12px}
.copyright{position:absolute;top:414px;width:100%;text-align:center;font-size:11px}
.to-top{position:absolute;left:1092px;top:406px;width:32px;height:32px;border-radius:50%;background:var(--white);display:flex;align-items:center;justify-content:center}
</style>
</head>
<body>

<header class="site-header">
  <div class="brand-badge"><span class="brand-name"><span class="dot"></span>Lumen Grove</span></div>
  <nav class="main-nav">
    <a class="active" href="#">Home</a><a href="#">How it works</a><a href="#">Products</a><a href="#">Pricing</a><a href="#">About us</a>
  </nav>
  <a class="btn nav-cta" href="#">Contact us</a>
</header>

<section class="hero" role="img" aria-label="Two analysts at a desk facing a large wall display of city data">
  <h1>Welcome to Lumen Grove</h1>
  <p>Lorem ipsum dolor sit amet, consectetur adipiscing elit, sed do us mod tempor incididunt ut labore et dolore magna aliqua.</p>
  <a class="btn" href="#">Get Started <span class="arrow"><svg viewBox="0 0 14 14"><path d="M5 3l4 4-4 4" fill="none" stroke="#7cb83a" stroke-width="2"/></svg></span></a>
  <div class="dots"><span></span><span></span><span></span><span></span></div>
</section>

<!-- products -->
<div class="kicker" style="top:876px">Products</div>
<h2 class="sec-title" style="top:910px">Cyber Security Products</h2>
<p class="sec-lead" style="top:986px">Lorem ipsum dolor sit amet, consectetur adipiscing elit. Nunc et urna ut libero dignissim faucibus a sit amet sapien. Donec condimentum massa sem, ac fermentum magna tincidunt et. Ut tortor est, imperdiet quis nulla quis.</p>

<article class="product-card" style="left:67px;top:1090px">
  <div class="media" role="img" aria-label="Hooded figure with a glowing hand over a digital network" style="background:linear-gradient(135deg,#0d1a3a,#1f5fb8 50%,#0a1226)"></div>
  <h3>PRODUCT 1</h3><h4>Lorem Ipsum Dolor sit ament</h4>
  <p>Lorem ipsum dolor sit amet, consectetur adipiscing elit. Praesent erat sem, placerat at placerat a, facilisis eget mauris.</p>
  <a class="btn" href="#">Read more <span class="arrow"><svg viewBox="0 0 14 14"><path d="M5 3l4 4-4 4" fill="none" stroke="#7cb83a" stroke-width="2.4"/></svg></span></a>
</article>
<article class="product-card" style="left:612px;top:1090px">
  <div class="media" role="img" aria-label="Glowing binary sphere among blue data rings" style="background:linear-gradient(135deg,#06152e,#2a6fb0 50%,#071a33)"></div>
  <h3>PRODUCT 2</h3><h4>Lorem Ipsum Dolor sit ament</h4>
  <p>Lorem ipsum dolor sit amet, consectetur adipiscing elit. Praesent erat sem, placerat at placerat a, facilisis eget mauris.</p>
  <a class="btn" href="#">Read more <span class="arrow"><svg viewBox="0 0 14 14"><path d="M5 3l4 4-4 4" fill="none" stroke="#7cb83a" stroke-width="2.4"/></svg></span></a>
</article>
<article class="product-card" style="left:67px;top:1561px">
  <div class="media" role="img" aria-label="Hands holding a tablet with a glowing padlock" style="background:linear-gradient(135deg,#1a2030,#5a7a9a 50%,#2a8ad6)"></div>
  <h3>PRODUCT 3</h3><h4>Lorem Ipsum Dolor sit ament</h4>
  <p>Lorem ipsum dolor sit amet, consectetur adipiscing elit. Praesent erat sem, placerat at placerat a, facilisis eget mauris.</p>
  <a class="btn" href="#">Read more <span class="arrow"><svg viewBox="0 0 14 14"><path d="M5 3l4 4-4 4" fill="none" stroke="#7cb83a" stroke-width="2.4"/></svg></span></a>
</article>
<article class="product-card" style="left:612px;top:1561px">
  <div class="media" role="img" aria-label="Person standing before a wall of data screens" style="background:linear-gradient(90deg,#2b4a66,#9ab6c9 50%,#4a3a22)"></div>
  <h3>PRODUCT 4</h3><h4>Lorem Ipsum Dolor sit ament</h4>
  <p>Lorem ipsum dolor sit amet, consectetur adipiscing elit. Praesent erat sem, placerat at placerat a, facilisis eget mauris.</p>
  <a class="btn" href="#">Read more <span class="arrow"><svg viewBox="0 0 14 14"><path d="M5 3l4 4-4 4" fill="none" stroke="#7cb83a" stroke-width="2.4"/></svg></span></a>
</article>
<a class="btn view-more" href="#">View more <span class="arrow"><svg viewBox="0 0 14 14"><path d="M5 3l4 4-4 4" fill="none" stroke="#000" stroke-width="2"/></svg></span></a>

<!-- how it works -->
<div class="kicker" style="top:2238px">Cyber Security</div>
<h2 class="sec-title" style="top:2280px">How It Works?</h2>
<p class="sec-lead" style="top:2346px">Lorem ipsum dolor sit amet, consectetur adipiscing elit. Nunc et urna ut libero dignissim faucibus a sit amet sapien. Donec condimentum massa sem, ac fermentum magna tincidunt et. Ut tortor est, imperdiet quis nulla quis.</p>

<div class="step" style="left:11px;top:2455px"><div class="ring"><span>1</span></div><h5>Firewalls</h5></div>
<div class="step" style="left:307px;top:2455px"><div class="ring"><span>2</span></div><h5>Encryption</h5></div>
<div class="step" style="left:608px;top:2455px"><div class="ring"><span>3</span></div><h5>Antivirus and<br>Anti-malware Software</h5></div>
<div class="step" style="left:904px;top:2455px"><div class="ring"><span>4</span></div><h5>Intrusion Detection<br>and Prevention<br>Systems (IDPS)</h5></div>
<svg class="step-arrow" style="left:205px" viewBox="0 0 150 40"><path d="M4 30 Q70 -6 140 28" fill="none" stroke="#7cb83a" stroke-width="2" stroke-dasharray="4 4"/><path d="M132 22l9 7-11 2" fill="none" stroke="#7cb83a" stroke-width="2"/></svg>
<svg class="step-arrow" style="left:505px" viewBox="0 0 150 40"><path d="M4 30 Q70 -6 140 28" fill="none" stroke="#7cb83a" stroke-width="2" stroke-dasharray="4 4"/><path d="M132 22l9 7-11 2" fill="none" stroke="#7cb83a" stroke-width="2"/></svg>
<svg class="step-arrow" style="left:805px" viewBox="0 0 150 40"><path d="M4 30 Q70 -6 140 28" fill="none" stroke="#7cb83a" stroke-width="2" stroke-dasharray="4 4"/><path d="M132 22l9 7-11 2" fill="none" stroke="#7cb83a" stroke-width="2"/></svg>

<!-- about -->
<div class="about-kicker">Who We Are</div>
<h2 class="about-title">About Lumen Grove</h2>
<p class="about-text">Lorem ipsum dolor sit amet, consectetur adipiscing elit. Nunc et urna ut libero dignissim faucibus a sit amet sapien. Donec condimentum massa sem, ac fermentum magna tincidunt et. Ut tortor est, imperdiet quis nulla quis, fringilla porttitor lectus. Sed euismod leo et est imperdiet, ut luctus nisi imperdiet. Donec dictum vitae mauris vitae rutrum.</p>
<a class="btn about-btn" href="#">Read more <span class="arrow"><svg viewBox="0 0 14 14"><path d="M5 3l4 4-4 4" fill="none" stroke="#7cb83a" stroke-width="2.4"/></svg></span></a>
<div class="about-visual" role="img" aria-label="Large photo-textured brand graphic"></div>

<!-- pricing -->
<div class="kicker" style="top:3268px">Pricing</div>
<h2 class="sec-title" style="top:3302px">Affordable Price Plans</h2>

<div class="plan" style="left:125px">
  <div class="head"><div class="price">$45.99</div><div class="per">/month</div></div>
  <ul>
    <li><i><svg width="14" height="14" viewBox="0 0 14 14"><path d="M3 7l3 3 5-6" fill="none" stroke="#7cb83a" stroke-width="2"/></svg></i>Lorem ipsum dolor sit</li>
    <li><i><svg width="14" height="14" viewBox="0 0 14 14"><path d="M3 7l3 3 5-6" fill="none" stroke="#7cb83a" stroke-width="2"/></svg></i>Lorem ipsum dolor sit</li>
    <li><i><svg width="14" height="14" viewBox="0 0 14 14"><path d="M3 7l3 3 5-6" fill="none" stroke="#7cb83a" stroke-width="2"/></svg></i>Lorem ipsum dolor sit</li>
    <li><i><svg width="14" height="14" viewBox="0 0 14 14"><path d="M3 7l3 3 5-6" fill="none" stroke="#7cb83a" stroke-width="2"/></svg></i>Lorem ipsum dolor sit</li>
  </ul>
  <a class="btn" href="#">Get Started</a>
</div>
<div class="plan featured" style="left:453px">
  <div class="head"><div class="price">$55.99</div><div class="per">/month</div></div>
  <ul>
    <li><i><svg width="14" height="14" viewBox="0 0 14 14"><path d="M3 7l3 3 5-6" fill="none" stroke="#fff" stroke-width="2"/></svg></i>Lorem ipsum dolor sit</li>
    <li><i><svg width="14" height="14" viewBox="0 0 14 14"><path d="M3 7l3 3 5-6" fill="none" stroke="#fff" stroke-width="2"/></svg></i>Lorem ipsum dolor sit</li>
    <li><i><svg width="14" height="14" viewBox="0 0 14 14"><path d="M3 7l3 3 5-6" fill="none" stroke="#fff" stroke-width="2"/></svg></i>Lorem ipsum dolor sit</li>
    <li><i><svg width="14" height="14" viewBox="0 0 14 14"><path d="M4 4l6 6M10 4l-6 6" fill="none" stroke="#fff" stroke-width="1.6"/></svg></i>Lorem ipsum dolor sit</li>
  </ul>
  <a class="btn" href="#">Get Started</a>
</div>
<div class="plan" style="left:779px">
  <div class="head"><div class="price">$99.99</div><div class="per">/month</div></div>
  <ul>
    <li><i><svg width="14" height="14" viewBox="0 0 14 14"><path d="M3 7l3 3 5-6" fill="none" stroke="#7cb83a" stroke-width="2"/></svg></i>Lorem ipsum dolor sit</li>
    <li><i><svg width="14" height="14" viewBox="0 0 14 14"><path d="M3 7l3 3 5-6" fill="none" stroke="#7cb83a" stroke-width="2"/></svg></i>Lorem ipsum dolor sit</li>
    <li><i><svg width="14" height="14" viewBox="0 0 14 14"><path d="M3 7l3 3 5-6" fill="none" stroke="#7cb83a" stroke-width="2"/></svg></i>Lorem ipsum dolor sit</li>
    <li><i><svg width="14" height="14" viewBox="0 0 14 14"><path d="M3 7l3 3 5-6" fill="none" stroke="#7cb83a" stroke-width="2"/></svg></i>Lorem ipsum dolor sit</li>
  </ul>
  <a class="btn" href="#">Get Started</a>
</div>

<!-- contact -->
<div class="contact-band"></div>
<div class="contact-visual"><div role="img" aria-label="Security operations desk with monitors"></div></div>
<div class="about-kicker" style="left:478px;top:3974px">Get In Touch</div>
<h2 class="about-title" style="left:478px;top:4004px">Contact Lumen Grove</h2>
<p class="abs" style="left:478px;top:4078px;font-size:13px">Lorem ipsum dolor sit amet, consectetur adipiscing elit. Nunc et urna ut libero dignissim.</p>
<div class="field" style="left:480px;top:4135px;width:256px">First Name:</div>
<div class="field" style="left:758px;top:4135px;width:255px">Last Name:</div>
<div class="field" style="left:480px;top:4210px;width:256px">Phone:</div>
<div class="field" style="left:758px;top:4210px;width:255px">Email:</div>
<div class="field" style="left:480px;top:4287px;width:533px;height:113px;padding-top:40px">Mesage:</div>
<a class="btn submit" href="#">Submit now <span class="arrow"><svg viewBox="0 0 14 14"><path d="M5 3l4 4-4 4" fill="none" stroke="#7cb83a" stroke-width="2"/></svg></span></a>

<!-- footer -->
<footer class="site-footer">
  <div class="foot-line" style="left:68px;top:125px;width:412px"></div>
  <div class="foot-line" style="left:720px;top:125px;width:413px"></div>
  <div class="foot-line" style="left:68px;top:224px;width:412px"></div>
  <div class="foot-line" style="left:720px;top:224px;width:413px"></div>
  <nav class="foot-nav" style="left:140px"><a href="#">How it works</a><i></i><a href="#">Products</a></nav>
  <div class="foot-brand"><span class="dot"></span>Lumen Grove</div>
  <nav class="foot-nav" style="left:849px"><a href="#">Pricing</a><i></i><a href="#">Contact us</a></nav>

  <div class="contact-item" style="left:67px"><span class="ic"><svg viewBox="0 0 24 24"><path d="M6 3l3 4-2 2a11 11 0 0 0 8 8l2-2 4 3-2 3C10 20 4 14 3 5z" fill="#000"/></svg></span><div><b>CALL US</b><small>0100 555 0142</small></div></div>
  <div class="contact-item" style="left:325px"><span class="ic"><svg viewBox="0 0 24 24"><rect x="3" y="6" width="18" height="12" fill="none" stroke="#000" stroke-width="2"/><path d="M3 6l9 7 9-7" fill="none" stroke="#000" stroke-width="2"/></svg></span><div><b>EMAIL US</b><small>info@lumengrove.example</small></div></div>
  <div class="contact-item" style="left:612px"><span class="ic"><svg viewBox="0 0 24 24"><path d="M12 2a7 7 0 0 0-7 7c0 5 7 13 7 13s7-8 7-13a7 7 0 0 0-7-7z" fill="#000"/><circle cx="12" cy="9" r="2.6" fill="#fff"/></svg></span><div><b>LOCATION 1</b><small>Address line dummy here</small></div></div>
  <div class="contact-item" style="left:897px"><span class="ic"><svg viewBox="0 0 24 24"><path d="M12 2a7 7 0 0 0-7 7c0 5 7 13 7 13s7-8 7-13a7 7 0 0 0-7-7z" fill="#000"/><circle cx="12" cy="9" r="2.6" fill="#fff"/></svg></span><div><b>LOCATION 2</b><small>Address line dummy here</small></div></div>

  <div class="foot-line" style="left:68px;top:383px;width:1065px"></div>
  <p class="copyright">Copyright © 2024 All Rights Reserved By Lumen Grove</p>
  <a class="to-top" href="#"><svg width="12" height="12" viewBox="0 0 12 12"><path d="M2 8l4-4 4 4" fill="none" stroke="#000" stroke-width="2"/></svg></a>
</footer>

</body>
</html>
```